Business Card Design Project

Black Writing

Jade Owlet

Target Market(s)

18 - 80 year olds

Industry/Entity Type

Business

Requirements
Must have
• Clean

```html
<!DOCTYPE html>
<html lang="en">
<head>
<meta charset="utf-8">
<title>Jade Owlet – Business Card</title>
<link rel="stylesheet" href="https://fonts.googleapis.com/css2?family=Arimo:wght@400;700&display=swap">
<style>
  :root {
    --page: #ececec;
    --card-top: #ffffff;
    --card-bottom: #ededed;
    --ink: #1c1c1c;
    --ink-soft: #333333;
    --gold: #a8874a;
    --band: #0d0d0d;
    --icon: #b08a4e;
    --mark-fill: #d9d9d9;
  }
  * { box-sizing: border-box; margin: 0; padding: 0; }
  html, body { width: 1200px; height: 900px; overflow: hidden; background: var(--page); }
  body { font-family: "Arimo", Arial, sans-serif; color: var(--ink); }

  .card {
    position: absolute; left: 100px; top: 165px;
    width: 1000px; height: 570px;
    border-radius: 34px; overflow: hidden;
    background: linear-gradient(180deg, var(--card-top) 0%, var(--card-bottom) 100%);
    box-shadow: 0 14px 40px rgba(0,0,0,.18);
  }
  .card-band { position: absolute; left: 0; bottom: 0; width: 1000px; height: 150px; }

  .partner-mark {
    position: absolute; left: 70px; top: 100px;
    display: flex; align-items: center; gap: 16px;
  }
  .partner-mark .dot { width: 56px; height: 56px; border-radius: 50%; background: var(--mark-fill); }
  .partner-mark .name { font-size: 32px; font-weight: 400; color: var(--ink); }

  .person { position: absolute; right: 62px; top: 62px; text-align: right; }
  .person .name { font-size: 28px; color: var(--gold); }
  .person .role { font-size: 20px; color: var(--ink-soft); margin-top: 6px; }

  .hours { position: absolute; right: 62px; top: 205px; text-align: right; font-size: 19px; line-height: 1.45; color: var(--ink-soft); }
  .hours .accent { color: var(--gold); }

  .brand-mark {
    position: absolute; right: 62px; top: 282px;
    display: flex; flex-direction: column; align-items: center; gap: 10px;
  }
  .brand-mark .dot {
    width: 100px; height: 100px; border-radius: 50%;
    background: var(--band);
  }
  .brand-mark .name { font-size: 28px; font-weight: 700; color: var(--ink); }

  .contacts { position: absolute; left: 68px; top: 292px; list-style: none; }
  .contacts li { display: flex; align-items: center; gap: 12px; font-size: 28px; line-height: 38px; color: var(--ink); }
  .contacts svg { width: 28px; height: 28px; flex: none; }
</style>
</head>
<body>
  <article class="card">
    <svg class="card-band" viewBox="0 0 1000 150" preserveAspectRatio="none" aria-hidden="true">
      <defs>
        <linearGradient id="goldLine" x1="0" x2="1">
          <stop offset="0" stop-color="#8c6a32"/>
          <stop offset=".5" stop-color="#f0d9a0"/>
          <stop offset="1" stop-color="#9c7a3e"/>
        </linearGradient>
      </defs>
      <path d="M0 92 C 300 80, 650 60, 1000 18 L1000 150 L0 150 Z" fill="url(#goldLine)"/>
      <path d="M0 100 C 300 88, 650 70, 1000 30 L1000 150 L0 150 Z" fill="var(--band)"/>
    </svg>

    <div class="partner-mark">
      <span class="dot"></span>
      <span class="name">Nile Lantern</span>
    </div>

    <div class="person">
      <p class="name">Mara Quell</p>
      <p class="role">Manager</p>
    </div>

    <div class="hours">
      <p>Mon - Sat : <span class="accent">Open</span></p>
      <p>5pm - 10pm : <span class="accent">Time</span></p>
    </div>

    <div class="brand-mark">
      <span class="dot"></span>
      <span class="name">Jade Owlet</span>
    </div>

    <ul class="contacts">
      <li>
        <svg viewBox="0 0 24 24" aria-hidden="true"><path fill="var(--icon)" d="M6.6 10.8a15.1 15.1 0 0 0 6.6 6.6l2.2-2.2c.3-.3.7-.4 1-.2 1.1.4 2.3.6 3.6.6.6 0 1 .4 1 1V20c0 .6-.4 1-1 1A17 17 0 0 1 3 4c0-.6.4-1 1-1h3.5c.6 0 1 .4 1 1 0 1.3.2 2.5.6 3.6.1.3 0 .7-.2 1z"/></svg>
        <span>1500 482 317</span>
      </li>
      <li>
        <svg viewBox="0 0 24 24" aria-hidden="true"><g fill="none" stroke="var(--icon)" stroke-width="2"><circle cx="12" cy="12" r="9"/><path d="M3 12h18M12 3c3 3.2 3 14.8 0 18M12 3c-3 3.2-3 14.8 0 18"/></g></svg>
        <span>www.jadeowlet.com</span>
      </li>
      <li>
        <svg viewBox="0 0 24 24" aria-hidden="true"><g fill="none" stroke="var(--icon)" stroke-width="2"><rect x="3" y="6" width="18" height="13" rx="1"/><path d="M3 7l9 7 9-7"/></g></svg>
        <span>info@jadeowlet.com</span>
      </li>
      <li>
        <svg viewBox="0 0 24 24" aria-hidden="true"><path fill="var(--icon)" d="M12 3 2 12h3v8h5v-5h4v5h5v-8h3z"/></svg>
        <span>PO Box 2741 Harbour Centre Qld 4370</span>
      </li>
    </ul>
  </article>
</body>
</html>
```